Laser Tattoo Removal Business Cards

We are looking for a professional business card design for a laser tattoo removal business. Ideally looking for a black business card design. The name of the business is Brightmoor Ink Erasure. We place our cards at local tattoo shops so we ideally are looking for something trendy/edgy to draw both male and female clientele in.

Target Market(s)

Male/Female ages 18-60

Contact Information for Business Card

black background ideally.. hoping to stay within greys, whites and black

Font styles to use
Serif
Sans Serif

Colors
121212
a9a9a9
5c5c5c
f5f5f5
ffffff
7f7f7f
606060
848484
9d9d9d

Requirements
Must have
• Employee Info:
• Melissa Danforth
• Chief Executive Offer
• m: 919.555.0143
• w: 919.555.0187
• f: 919.555.0162
• mdanforth@brightmoorinkerasure.com
• Address:
• 4518 Pell Ridge Dr, Suite 210
• Raleigh, NC 27699
• Website:
• www.brightmoorinkerasure.com
Nice to have
• Myabe business name on back or logo on back and employee info on the front

```html
<!DOCTYPE html>
<html lang="en">
<head>
<meta charset="utf-8">
<title>Brightmoor Ink Erasure – Business Cards</title>
<link rel="stylesheet" href="https://fonts.googleapis.com/css2?family=Figtree:wght@400;500;600&family=Montserrat:wght@500&display=swap">
<style>
  :root {
    --backdrop: #2b2b2b;
    --card: #ffffff;
    --ink: #121212;
    --ink-soft: #5c5c5c;
    --ink-mid: #606060;
    --rule: #7f7f7f;
    --fade-light: #f5f5f5;
    --fade-mid: #9d9d9d;
    --fade-dark: #121212;
  }
  * { box-sizing: border-box; margin: 0; padding: 0; }
  html, body { width: 1200px; height: 960px; overflow: hidden; }
  body {
    background: var(--backdrop);
    font-family: "Figtree", Arial, sans-serif;
    position: relative;
  }
  .card {
    position: absolute;
    left: 220px;
    width: 760px;
    height: 420px;
    background: var(--card);
    border-radius: 22px;
    overflow: hidden;
  }
  .card--front { top: 50px; }
  .card--back { top: 500px; }

  .brand-name {
    position: absolute;
    text-align: center;
    font-family: "Montserrat", Arial, sans-serif;
    font-weight: 500;
    font-size: 30px;
    line-height: 1.2;
    letter-spacing: 2px;
    text-transform: uppercase;
    color: var(--ink);
    white-space: nowrap;
  }
  .card--front .brand-name { left: 60px; width: 300px; top: 228px; }
  .card--back .brand-name { left: 470px; width: 280px; top: 58px; z-index: 2; }

  .divider {
    position: absolute;
    left: 380px; top: 75px;
    width: 2px; height: 276px;
    background: var(--rule);
  }
  .contact {
    position: absolute;
    left: 416px; top: 66px;
    width: 326px;
    color: var(--ink-soft);
  }
  .contact__name {
    font-size: 26px;
    font-weight: 600;
    letter-spacing: 0.2px;
    color: var(--ink);
    text-transform: uppercase;
    white-space: nowrap;
  }
  .contact__title {
    font-size: 19.5px;
    margin-top: 4px;
    color: var(--ink-mid);
  }
  .contact__address {
    font-size: 17px;
    line-height: 26px;
    margin-top: 34px;
  }
  .contact__list {
    list-style: none;
    margin-top: 16px;
    font-size: 16.5px;
  }
  .contact__list li {
    display: flex;
    align-items: center;
    height: 25.7px;
    white-space: nowrap;
  }
  .contact__list svg {
    width: 13px; height: 13px;
    margin-right: 9px;
    fill: var(--ink);
    flex: none;
  }
  .contact__list .web-domain { color: var(--ink); }

  .photo-area {
    position: absolute;
    left: 0; right: 0; top: 140px; bottom: 0;
    background:
      linear-gradient(180deg, rgba(255,255,255,0.9) 0%, rgba(255,255,255,0) 40%),
      linear-gradient(100deg, #3a3a3a 0%, var(--fade-mid) 32%, var(--fade-light) 62%, #d9d9d9 80%, var(--fade-dark) 100%);
  }
  .photo-area::after {
    content: "";
    position: absolute; inset: 0;
    background: linear-gradient(0deg, rgba(18,18,18,0.75) 0%, rgba(18,18,18,0) 45%);
  }
</style>
</head>
<body>

<section class="card card--front">
  <p class="brand-name">Brightmoor<br>Ink Erasure</p>
  <div class="divider"></div>
  <div class="contact">
    <h1 class="contact__name">Melissa Danforth</h1>
    <p class="contact__title">Chief Executive Offer</p>
    <p class="contact__address">4518 Pell Ridge Dr, Suite 210<br>Raleigh, NC 27699</p>
    <ul class="contact__list">
      <li><svg viewBox="0 0 16 16"><path d="M4 0h8a1 1 0 0 1 1 1v14a1 1 0 0 1-1 1H4a1 1 0 0 1-1-1V1a1 1 0 0 1 1-1zm1 2v10h6V2z"/></svg>919.555.0143</li>
      <li><svg viewBox="0 0 16 16"><path d="M3.5 1l2.5 3-1.5 2c1 2 3 4 5 5l2-1.5 3 2.5-1.5 2.5C7 15 1 9 1 2.5z"/></svg>919.555.0187</li>
      <li><svg viewBox="0 0 16 16"><path d="M4 1h7l1 1v3H4zM1 6h14v6h-3v3H4v-3H1zm5 5v2h4v-2z"/></svg>919.555.0162</li>
      <li><svg viewBox="0 0 16 16"><path d="M1 3h14v10H1zm1.5 1.5L8 9l5.5-4.5z" fill-rule="evenodd"/></svg>mdanforth@brightmoorinkerasure.com</li>
      <li><svg viewBox="0 0 16 16"><circle cx="8" cy="8" r="7"/><path d="M1 8h14M8 1c3 3 3 11 0 14M8 1c-3 3-3 11 0 14" stroke="#fff" stroke-width="1" fill="none"/></svg>www.<span class="web-domain">brightmoorinkerasure</span>.com</li>
    </ul>
  </div>
</section>

<section class="card card--back">
  <div class="photo-area" role="img" aria-label="Photo of a technician in gloves performing laser tattoo removal on a client's hip, fading into white at the top"></div>
  <p class="brand-name">Brightmoor<br>Ink Erasure</p>
</section>

</body>
</html>
```